Stationery Design Project

Brivan-Holt Consultants is interim management company. We are specialized in finding the best Finance and IT consultants for our clients when they require additional resources on an interim basis for projects or special situations. We are flexible in our approach and we always seek to maximize the benefits for our clients as well as our consultants.

We are looking for a design of our letterhead, general stationery and business cards using the company name. The design will also be found on our coming web pages.
Updates

Please also create a logo for Brivan-Holt Consultants which expresses that we want to match the best finance and IT people to our customers projects

Target Market(s)

Larger and mid sized companies (all sectors), as well as highly skilled Finance & IT professionals/consultants

Industry/Entity Type

Business

Requirements
Must have
• Brivan-Holt Consultants
We are expecting that 'Brivan-Holt' will be on the first line and 'Consultants' on a second line.
Please also indicate style of the letters for our address/phone and mail details. Our current address is:
Tarnvoldgade 9,
2870 Kalsbro
Danmark
Mobile: +45 XX XX XX XX Mail: xx@brivan-holt.dk

```html
<!DOCTYPE html>
<html lang="en">
<head>
<meta charset="utf-8">
<title>Brivan-Holt Consultants – Business Card</title>
<link href="https://fonts.googleapis.com/css2?family=Tinos:wght@400;700&display=swap" rel="stylesheet">
<style>
  :root {
    --backdrop: #3b3b3b;
    --card-light: #ffffff;
    --card-edge: #d9d9d9;
    --brand-red: #ee1c25;
    --mark-grey: #666666;
    --text-grey: #555555;
    --text-red: #e8372c;
  }
  * { margin: 0; padding: 0; box-sizing: border-box; }
  html, body { width: 1200px; height: 534px; overflow: hidden; }
  body {
    background: var(--backdrop);
    font-family: "Tinos", "Times New Roman", serif;
    position: relative;
  }
  .card {
    position: absolute;
    top: 123px;
    width: 502px;
    height: 288px;
    border-radius: 16px;
    overflow: hidden;
    background: radial-gradient(ellipse at 55% 40%, var(--card-light) 0%, #f3f3f3 45%, var(--card-edge) 100%);
  }
  .card--front { left: 90px; }
  .card--back { left: 611px; }

  .accent-area {
    position: absolute;
    left: 0;
    top: 96px;
    width: 290px;
    height: 192px;
    background: linear-gradient(to top right, var(--brand-red) 0%, rgba(238, 28, 37, 0.75) 45%, rgba(238, 28, 37, 0) 100%);
  }

  .brand { position: absolute; display: flex; align-items: center; color: var(--brand-red); }
  .brand__square { background: var(--mark-grey); flex: none; }
  .brand__name { font-weight: 400; line-height: 1; text-transform: uppercase; }
  .brand__sub { display: block; letter-spacing: 0.3em; }

  .card--front .brand { left: 25px; top: 28px; gap: 10px; }
  .card--front .brand__square { width: 34px; height: 34px; }
  .card--front .brand__name { font-size: 21px; }
  .card--front .brand__sub { font-size: 8px; margin-top: 2px; }

  .contact {
    position: absolute;
    left: 304px;
    top: 168px;
    font-size: 12.5px;
    line-height: 13.6px;
    color: var(--text-grey);
  }
  .contact__name { color: var(--text-red); font-size: 14px; line-height: 16px; }
  .contact__position { margin-bottom: 14px; }
  .contact__label { color: var(--text-red); }

  .card--back .brand { left: 83px; top: 96px; gap: 14px; }
  .card--back .brand__square { width: 76px; height: 76px; }
  .card--back .brand__name { font-size: 38px; }
  .card--back .brand__sub { font-size: 12px; margin-top: 4px; letter-spacing: 0.45em; }

  .website {
    position: absolute;
    left: 0; right: 0;
    top: 238px;
    text-align: center;
    font-size: 14px;
    letter-spacing: 0.3em;
    color: var(--text-grey);
  }
  .website__name { color: var(--text-red); }
</style>
</head>
<body>
  <section class="card card--front" aria-label="Business card front">
    <div class="accent-area" role="img" aria-label="Decorative red accent sweeping across the lower left of the card"></div>
    <div class="brand">
      <span class="brand__square"></span>
      <span class="brand__name">Brivan-Holt<span class="brand__sub">Consultants</span></span>
    </div>
    <div class="contact">
      <p class="contact__name">Consultant Name</p>
      <p class="contact__position">Position</p>
      <p>Tarnvoldgade 9,</p>
      <p>2870 Kalsbro, Danmark</p>
      <p><span class="contact__label">Mobile:</span> + 45 XX XX XX XX</p>
      <p><span class="contact__label">Email:</span> xx@brivan-holt.dk</p>
      <p><span class="contact__label">Website:</span> www.brivan-holt.dk</p>
    </div>
  </section>

  <section class="card card--back" aria-label="Business card back">
    <div class="brand">
      <span class="brand__square"></span>
      <span class="brand__name">Brivan-Holt<span class="brand__sub">Consultants</span></span>
    </div>
    <p class="website">WWW.<span class="website__name">BRIVAN-HOLT</span>.DK</p>
  </section>
</body>
</html>
```